Quillory Nest Business Card

I need a business card design. We are a collaborate online training company. Our colors are gray and green. Our website is QuilloryNest.com

I would like an area for a profile picture within the card

```html
<!DOCTYPE html>
<html lang="en">
<head>
<meta charset="utf-8">
<title>Quillory Nest Business Card</title>
<link href="https://fonts.googleapis.com/css2?family=Montserrat:wght@400;500;700;800&display=swap" rel="stylesheet">
<style>
  :root {
    --green: #8dc63f;
    --black: #111111;
    --white: #ffffff;
    --ink: #1a1a1a;
    --stage: #e9ebe8;
    --photo-a: #9aa79a;
    --photo-b: #5c615e;
  }
  * { margin: 0; padding: 0; box-sizing: border-box; }
  html, body { width: 1200px; height: 900px; overflow: hidden; }
  body {
    background: var(--stage);
    font-family: "Montserrat", sans-serif;
    position: relative;
  }
  .card {
    position: absolute;
    left: 250px;
    width: 700px;
    height: 400px;
    border-radius: 26px;
    overflow: hidden;
    box-shadow: 0 10px 30px rgba(0,0,0,.18);
  }
  .card-front { top: 35px; background: var(--green); }
  .card-back { top: 465px; background: var(--white); }

  .brand {
    display: flex; align-items: center; gap: 10px;
    font-weight: 800; color: var(--ink); letter-spacing: -0.5px;
    white-space: nowrap; line-height: 1;
  }
  .brand-dot { border-radius: 50%; flex: none; }

  /* front */
  .profile-photo {
    position: absolute;
    left: 110px; bottom: 26px;
    width: 280px; height: 300px;
    background: linear-gradient(180deg, var(--photo-a), var(--photo-b));
    border-radius: 140px 140px 0 0;
  }
  .card-front .brand { position: absolute; left: 420px; top: 150px; font-size: 30px; }
  .card-front .brand-dot { width: 34px; height: 34px; background: var(--white); }
  .front-web {
    position: absolute; right: 60px; top: 258px;
    color: var(--white); font-size: 16px; font-weight: 500;
  }
  .front-strip {
    position: absolute; left: 0; right: 0; bottom: 0; height: 26px;
    background: var(--white);
  }
  .front-strip-dark {
    position: absolute; right: 0; bottom: 0; width: 270px; height: 26px;
    background: var(--black);
    clip-path: polygon(18px 0, 100% 0, 100% 100%, 0 100%);
  }

  /* back */
  .card-back .brand { position: absolute; left: 50px; top: 112px; font-size: 36px; }
  .card-back .brand-dot { width: 42px; height: 42px; background: var(--green); }
  .person { position: absolute; right: 55px; top: 90px; text-align: right; }
  .person-name { color: var(--green); font-size: 28px; font-weight: 800; letter-spacing: 0.5px; }
  .person-role { color: var(--ink); font-size: 14px; font-weight: 500; letter-spacing: 1px; }
  .rule-name {
    position: absolute; left: 300px; right: 55px; top: 168px;
    height: 3px; background: var(--green);
  }
  .address {
    position: absolute; right: 55px; top: 185px; text-align: right;
    color: var(--ink); font-size: 16px; line-height: 1.5;
  }
  .rule-contact {
    position: absolute; left: 50px; width: 300px; top: 268px;
    height: 3px; background: var(--green);
  }
  .contacts {
    position: absolute; left: 50px; top: 280px;
    list-style: none; color: var(--ink); font-size: 16px; line-height: 1.6;
  }
  .contacts li { display: flex; align-items: center; gap: 10px; }
  .contacts svg { width: 14px; height: 14px; fill: var(--green); flex: none; }
  .contacts .accent { color: var(--green); }
  .back-band {
    position: absolute; left: 260px; bottom: 0; width: 230px; height: 24px;
    background: var(--green);
  }
  .back-band-dark {
    position: absolute; right: 0; bottom: 0; width: 210px; height: 24px;
    background: var(--black);
  }
</style>
</head>
<body>
  <section class="card card-front">
    <div class="profile-photo" role="img" aria-label="Portrait photo of the founder"></div>
    <div class="brand"><span class="brand-dot"></span>QuilloryNest</div>
    <p class="front-web">www.quillorynest.com</p>
    <div class="front-strip"></div>
    <div class="front-strip-dark"></div>
  </section>

  <section class="card card-back">
    <div class="brand"><span class="brand-dot"></span>QuilloryNest</div>
    <div class="person">
      <p class="person-name">DORIAN PELL</p>
      <p class="person-role">FOUNDER</p>
    </div>
    <div class="rule-name"></div>
    <p class="address">480 W Marlow Ave. Suite 7<br>Fenwick, Arizona 85390</p>
    <div class="rule-contact"></div>
    <ul class="contacts">
      <li><svg viewBox="0 0 24 24"><path d="M6.6 10.8a15 15 0 0 0 6.6 6.6l2.2-2.2a1 1 0 0 1 1-.25 11.4 11.4 0 0 0 3.6.57 1 1 0 0 1 1 1V20a1 1 0 0 1-1 1A17 17 0 0 1 3 4a1 1 0 0 1 1-1h3.5a1 1 0 0 1 1 1c0 1.25.2 2.45.57 3.57a1 1 0 0 1-.25 1z"/></svg>(302) 555-0147</li>
      <li><svg viewBox="0 0 24 24"><path d="M2 5h20v14H2zm2 2v.5l8 5 8-5V7l-8 5z"/></svg>info@quillorynest.com</li>
      <li><svg viewBox="0 0 24 24"><circle cx="12" cy="12" r="10"/></svg><span>www.<span class="accent">quillorynest</span>.com</span></li>
    </ul>
    <div class="back-band"></div>
    <div class="back-band-dark"></div>
  </section>
</body>
</html>
```